Property development company needs a name card design

I started my company since 2010, based in Auckland, New Zealand. We have been doing residential property rentals, individual low-rise residential property construction, small to medium scale residential development project. We will be participate in property investment as well. I have no favor of any specific design or color, just be creative and do anything you think will match the concept.

```html
<!DOCTYPE html>
<html lang="en">
<head>
<meta charset="utf-8">
<title>Northcote Property &amp; Building — Name Cards</title>
<link rel="stylesheet" href="https://fonts.googleapis.com/css2?family=Alice&family=Oswald:wght@600&family=Source+Sans+3:wght@400;700&display=swap">
<style>
  :root {
    --brand-red: #ee1c25;
    --ink: #111111;
    --card-edge: #222222;
    --paper: #ffffff;
  }
  * { box-sizing: border-box; margin: 0; padding: 0; }
  html, body { width: 1200px; height: 846px; overflow: hidden; background: var(--paper); }
  .sheet { position: relative; width: 1200px; height: 846px; }
  .card {
    position: absolute;
    border: 2px solid var(--card-edge);
    background: var(--paper);
    overflow: hidden;
    color: var(--ink);
  }
  .brand {
    position: absolute;
    display: flex;
    flex-direction: column;
    align-items: center;
    text-align: center;
  }
  .brand-dot { border-radius: 50%; background: var(--brand-red); }
  .brand-name {
    font-family: "Alice", Georgia, serif;
    font-weight: 400;
    color: var(--ink);
    line-height: 1.08;
    white-space: nowrap;
  }
  .holder-name {
    font-family: "Oswald", "Arial Narrow", sans-serif;
    font-weight: 600;
    letter-spacing: 0.5px;
    line-height: 1;
  }
  .holder-name .first { color: var(--brand-red); }
  .contact {
    font-family: "Source Sans 3", Arial, sans-serif;
    line-height: 1.35;
  }
  .contact.serif-lines { font-family: "Alice", Georgia, serif; }
  .contact b { font-family: "Source Sans 3", Arial, sans-serif; font-weight: 700; }
  .divider { position: absolute; width: 2px; background: var(--ink); }
  .corner-dot { position: absolute; border-radius: 50%; background: var(--brand-red); }

  /* card positions */
  .card-landscape-split { left: 531px; top: 0; width: 559px; height: 300px; }
  .card-portrait { left: 1px; top: 288px; width: 303px; height: 549px; }
  .card-front-a { left: 358px; top: 345px; width: 413px; height: 224px; }
  .card-front-b { left: 787px; top: 345px; width: 412px; height: 224px; }
  .card-back-stacked { left: 358px; top: 613px; width: 413px; height: 221px; }
  .card-back-inline { left: 787px; top: 613px; width: 412px; height: 221px; }
</style>
</head>
<body>
<main class="sheet">

  <section class="card card-landscape-split">
    <div class="brand" style="left:30px; top:62px; width:240px;">
      <div class="brand-dot" style="width:110px; height:110px; margin-bottom:10px;"></div>
      <div class="brand-name" style="font-size:22px;">Northcote Property<br>&amp; Building LTD</div>
    </div>
    <div class="divider" style="left:278px; top:48px; height:202px;"></div>
    <div style="position:absolute; left:308px; top:52px;">
      <h1 class="holder-name" style="font-size:28px; margin-bottom:24px;">LUCY WANG</h1>
      <p class="contact" style="font-size:16.5px; line-height:1.38;">
        <b>Address:</b> Level 2,<br>48 Kereru Road,<br>Riverside Village, Auckland<br>
        <b>Mobile:</b> 021 000 4567<br><b>Website:</b> npb-nz.co<br><b>Email:</b> lucywang@npb-nz.co
      </p>
    </div>
  </section>

  <section class="card card-portrait">
    <div class="brand" style="left:0; top:42px; width:299px;">
      <div class="brand-dot" style="width:96px; height:96px; margin-bottom:10px;"></div>
      <div class="brand-name" style="font-size:22px;">Northcote Property<br>&amp; Building LTD</div>
    </div>
    <div style="position:absolute; left:34px; top:346px;">
      <h2 class="holder-name" style="font-size:28px; margin-bottom:16px;">LUCY WANG</h2>
      <p class="contact" style="font-size:16.5px; line-height:1.38;">
        <b>Address:</b> Level 2,<br>48 Kereru Road,<br>Riverside Village, Auckland<br>
        <b>Mobile:</b> 0210004567<br><b>Website:</b> npb-nz.co<br><b>Email:</b> lucywang@npb-nz.co
      </p>
    </div>
  </section>

  <section class="card card-front-a">
    <div class="brand" style="left:0; top:22px; width:409px;">
      <div class="brand-dot" style="width:112px; height:112px; margin-bottom:10px;"></div>
      <div class="brand-name" style="font-size:28px;">Northcote Property<br>&amp; Building LTD</div>
    </div>
  </section>

  <section class="card card-front-b">
    <div class="brand" style="left:0; top:22px; width:408px;">
      <div class="brand-dot" style="width:112px; height:112px; margin-bottom:10px;"></div>
      <div class="brand-name" style="font-size:28px;">Northcote Property<br>&amp; Building LTD</div>
    </div>
  </section>

  <section class="card card-back-stacked">
    <p class="contact serif-lines" style="position:absolute; left:16px; top:12px; font-size:15.5px; line-height:1.47;">
      <b>Address:</b> Level 2,<br>48 Kereru Road,<br>Riverside Village, Auckland<br>
      <b>Mobile:</b> 021 000 4567<br><b>Website:</b> npb-nz.co<br><b>Email:</b> lucywang@npb-nz.co
    </p>
    <h2 class="holder-name" style="position:absolute; right:22px; top:20px; font-size:36px; line-height:1.2; text-align:left;">
      <span class="first">LUCY</span><br>WANG
    </h2>
    <div class="corner-dot" style="left:262px; top:132px; width:126px; height:126px;"></div>
  </section>

  <section class="card card-back-inline">
    <h2 class="holder-name" style="position:absolute; left:22px; top:18px; font-size:30px;">
      <span class="first">LUCY</span> WANG
    </h2>
    <p class="contact serif-lines" style="position:absolute; left:22px; top:72px; font-size:15.5px; line-height:1.47;">
      <b>Address:</b> Level 2,<br>48 Kereru Road,<br>Riverside Village, Auckland<br>
      <b>Mobile:</b> 021 000 4567<br><b>Website:</b> npb-nz.co<br><b>Email:</b> lucywang@npb-nz.co
    </p>
    <div class="corner-dot" style="left:268px; top:132px; width:126px; height:126px;"></div>
  </section>

</main>
</body>
</html>
```